Meridian Handsets business card design

I would like to see some designs for a business card for Meridian Handsets. I would like the business card to be double sided. It will need to have a similar colour / look and feel to our website www.meridianhandsets.com.au I have also attached our latest flyer. Final designs to be handed over in Photoshop format so that I can edit the business card when needed please.

Industry/Entity Type

Business

Contact Information for Business Card

Gavin Thornley
sales@meridianhandsets.com.au
Business Development Manager
ph: (08) 6197 5821
www.meridianhandsets.com.au

Font styles to use
Serif
Sans Serif

Requirements
Must have
• If you could please utilise our colour scheme as seen on our website and the attached flyer.
• I would also like the final design to be in a Photoshop format so that I can edit it when needed please.

```html
<!DOCTYPE html>
<html lang="en">
<head>
<meta charset="utf-8">
<title>Meridian Handsets — Business Card</title>
<link rel="stylesheet" href="https://fonts.googleapis.com/css2?family=Montserrat:wght@500&family=Roboto:wght@400&display=swap">
<style>
  :root {
    --backdrop: #2b2624;
    --card: #1c1c1d;
    --card-edge: #141415;
    --ink-white: #f4f4f4;
    --ink-blue: #1677c2;
    --ink-grey: #cfcfcf;
  }
  * { box-sizing: border-box; margin: 0; padding: 0; }
  html, body {
    width: 1200px; height: 780px; overflow: hidden;
    background: var(--backdrop);
  }
  .canvas {
    position: relative; width: 1200px; height: 780px;
  }
  .card {
    position: absolute;
    width: 540px; height: 310px;
    background: var(--card);
    border: 1px solid var(--card-edge);
    border-radius: 3px;
    box-shadow: 0 10px 30px rgba(0,0,0,0.45);
  }
  .card--front { left: 40px; top: 235px; }
  .card--back  { left: 620px; top: 235px; }

  .brand {
    font-family: "Montserrat", sans-serif;
    font-weight: 500;
    color: var(--ink-white);
    letter-spacing: 0.5px;
    white-space: nowrap;
    display: flex; align-items: center; gap: 12px;
  }
  .brand__dot {
    width: 12px; height: 12px; border-radius: 50%;
    background: var(--ink-white);
    flex: none;
  }
  .card--front .brand {
    position: absolute; left: 40px; top: 34px; font-size: 34px;
  }
  .card--back .brand {
    position: absolute; left: 0; right: 0; top: 128px;
    justify-content: center; font-size: 42px;
  }

  .rule {
    position: absolute; left: 0; top: 100px;
    width: 300px; height: 1px; background: var(--ink-white);
  }

  .person {
    position: absolute; right: 36px; top: 116px; text-align: right;
    font-family: "Roboto", sans-serif;
  }
  .person__name { color: var(--ink-blue); font-size: 21px; line-height: 1.2; }
  .person__title { color: var(--ink-white); font-size: 14px; margin-top: 2px; }

  .contact {
    position: absolute; left: 36px; bottom: 46px;
    list-style: none;
    font-family: "Roboto", sans-serif; font-size: 13px; color: var(--ink-grey);
  }
  .contact__item { display: flex; align-items: center; gap: 10px; line-height: 22px; }
  .contact__icon { width: 12px; height: 12px; flex: none; }
</style>
</head>
<body>
<main class="canvas">

  <section class="card card--front" aria-label="Card front">
    <div class="brand"><span>Meridian Handsets</span></div>
    <div class="rule"></div>
    <div class="person">
      <p class="person__name">Gavin Thornley</p>
      <p class="person__title">Business Development Manager</p>
    </div>
    <ul class="contact">
      <li class="contact__item">
        <svg class="contact__icon" viewBox="0 0 12 12" aria-hidden="true">
          <rect x="0.5" y="0.5" width="11" height="11" fill="none" stroke="#1677c2"/>
          <path d="M3.5 3h1.5l.6 1.6-.9.6a4 4 0 0 0 2 2l.6-.9 1.6.6V8.5A1 1 0 0 1 8 9.5 5.5 5.5 0 0 1 2.5 4 1 1 0 0 1 3.5 3z" fill="#1677c2"/>
        </svg>
        <span>(08) 6197 5821</span>
      </li>
      <li class="contact__item">
        <svg class="contact__icon" viewBox="0 0 12 12" aria-hidden="true">
          <rect x="0.5" y="0.5" width="11" height="11" fill="none" stroke="#1677c2"/>
          <circle cx="6" cy="6" r="3.2" fill="none" stroke="#1677c2"/>
          <path d="M2.8 6h6.4M6 2.8v6.4" stroke="#1677c2" stroke-width="0.8"/>
        </svg>
        <span>www.meridianhandsets.com.au</span>
      </li>
      <li class="contact__item">
        <svg class="contact__icon" viewBox="0 0 12 12" aria-hidden="true">
          <rect x="0.5" y="0.5" width="11" height="11" fill="#1677c2"/>
          <path d="M2.5 4l3.5 2.5L9.5 4" fill="none" stroke="#1c1c1d" stroke-width="1"/>
        </svg>
        <span>sales@meridianhandsets.com.au</span>
      </li>
    </ul>
  </section>

  <section class="card card--back" aria-label="Card back">
    <div class="brand"><span>Meridian Handsets</span></div>
  </section>

</main>
</body>
</html>
```